Herausgeber suchen Design
Zielgruppe
Wir sind Herausgeber einer Festschrift für unseren Doktor-/Habilvater, Prof. Dr. Lohmeyer, und suchen ein hochwertiges Design für die Einladungskarten zu einem Symposium, im Rahmen dessen die Festschrift übergeben wird; Zielgruppe sind die Autoren der Festschrift, Alumnis und Weggefährten von Herrn Lohmeyer
Aufgabenstellung
- Maße: 210 mm x 105 mm
- Einladungskarte: geklappt; Frontseite, 2 Innenseiten, Rückseite
- Zum Text siehe Datei 'Text Einladungskarte'
- Design eher traditionell/konservativ, da es sich um einen wissenschaftlichen Hintergrund handelt (Symposium, Übergabe Festschrift)
- Die Farben sollen mit dem Cover der Festschrift korrespondieren (vgl. Datei 'Templates_Research_Vossek', dort das erste Cover (KLM_RE_T01)

```html
<!DOCTYPE html>
<html lang="de">
<head>
<meta charset="utf-8">
<title>Einladung Symposium</title>
<link href="https://fonts.googleapis.com/css2?family=Hind:wght@400;500;600&family=Pinyon+Script&display=swap" rel="stylesheet">
<style>
  :root {
    --stage: #e6e6e6;
    --navy: #1e3a68;
    --accent: #1a80c4;
    --paper: #ffffff;
    --ink: #1a1a1a;
    --muted: #707070;
    --rule: #9a9a9a;
    --fold: #d4d4d4;
    --ghost: #e9eef8;
  }
  * { margin: 0; padding: 0; box-sizing: border-box; }
  html, body { width: 1200px; height: 936px; overflow: hidden; background: var(--stage); }
  body { position: relative; font-family: "Hind", sans-serif; color: var(--ink); }

  .panel { position: absolute; }
  .front { left: 600px; top: 15px; width: 580px; height: 290px; background: var(--navy); overflow: hidden; }
  .front__band { position: absolute; left: 0; right: 0; top: 185px; height: 7px; background: var(--accent); }
  .front__title {
    position: absolute; left: 320px; top: 128px;
    font-family: "Pinyon Script", cursive; font-size: 52px; line-height: 1; color: #fff;
  }
  .back { left: 19px; top: 627px; width: 581px; height: 291px; background: var(--navy); }

  .inside { left: 19px; top: 321px; width: 1161px; height: 290px; background: var(--paper); overflow: hidden; }
  .inside__fold { position: absolute; left: 581px; top: 0; bottom: 0; width: 1px; background: var(--fold); }
  .inside__ghost {
    position: absolute; left: 92px; top: 100px;
    font-family: "Pinyon Script", cursive; font-size: 150px; line-height: 1;
    color: var(--ghost); white-space: nowrap; letter-spacing: 6px;
  }

  .txt { position: absolute; font-size: 9.6px; line-height: 11.8px; white-space: nowrap; }
  .muted { color: var(--muted); font-weight: 600; }
  .rule { position: absolute; height: 1px; background: var(--rule); }

  .intro__lead { left: 139px; top: 41px; font-size: 10.2px; }
  .intro__name { left: 139px; top: 54px; font-size: 14.5px; line-height: 18px; font-weight: 600; }
  .intro .rule { left: 139px; width: 354px; }
  .intro__when { left: 139px; top: 93px; }
  .intro__editors-label { left: 139px; top: 151px; }
  .intro__editors { left: 174px; top: 175px; }
  .intro__closing { left: 139px; top: 245px; }

  .agenda__label { left: 719px; top: 41px; font-style: italic; }
  .agenda .txt.item { left: 755px; }
  .agenda .rule { left: 755px; width: 355px; }
  .agenda__rsvp { left: 719px; top: 249px; font-style: italic; }
  .highlight { color: var(--muted); font-weight: 600; }
</style>
</head>
<body>

  <section class="panel front">
    <div class="front__band"></div>
    <div class="front__title">Einladung</div>
  </section>

  <section class="panel inside">
    <div class="inside__ghost">Symposium</div>
    <div class="inside__fold"></div>

    <div class="intro">
      <p class="txt intro__lead muted">Symposium anlässlich der Übergabe der Festschrift an</p>
      <h1 class="txt intro__name">Prof. Dr. Hans-Joachim Lohmeyer</h1>
      <div class="rule" style="top:86px"></div>
      <p class="txt intro__when">am 29.06.2018 um 16 Uhr<br>im Gästehaus der Universität Nordhafen,<br>Lindenallee 12, 20100 Nordhafen</p>
      <div class="rule" style="top:138px"></div>
      <p class="txt intro__editors-label">Die Herausgeber</p>
      <p class="txt intro__editors">Prof. Dr. Martin Kessler<br>Prof. Dr. Jonas Berghoff<br>Prof. Dr. Thomas R. Albrecht, StB<br>PD Dr. Henrik Ostendorf<br>Dr. Lukas Brandner</p>
      <p class="txt intro__closing">laden herzlich ein.</p>
    </div>

    <div class="agenda">
      <p class="txt agenda__label">Ablauf</p>
      <p class="txt item" style="top:65px"><span class="muted">Begrüßung und Vorstellung der Festschrift</span><br>Prof. Dr. Martin Kessler</p>
      <div class="rule" style="top:94px"></div>
      <p class="txt item" style="top:100px"><span class="muted">«Fortentwicklung des Corporate Governance Reportings»</span><br>Prof. Dr. Felix M. Harmsen, LL.M. (London)</p>
      <div class="rule" style="top:132px"></div>
      <p class="txt item muted" style="top:136px">Diskussion</p>
      <div class="rule" style="top:153px"></div>
      <p class="txt item" style="top:158px"><span class="muted">«Neuere Entwicklungen im Rahmen der risikoorientierten Abschlussprüfung»</span><br>Prof. Dr. Jakob W. Reiter</p>
      <div class="rule" style="top:189px"></div>
      <p class="txt item muted" style="top:194px">Diskussion</p>
      <div class="rule" style="top:212px"></div>
      <p class="txt item" style="top:217px">Im Anschluss an das Symposium findet ein <span class="highlight">Umtrunk</span> statt.</p>
      <p class="txt agenda__rsvp">Um Antwort wird gebeten bis zum 18. Mai 2018 unter clara.weiss@wiso.uni-nordhafen.de</p>
    </div>
  </section>

  <section class="panel back"></section>

</body>
</html>
```